Blow Dry Bar Business Cards

These cards must be eye catching and modern.
You must be willing to work fast and make changes.

Winner will be offered other projects

Files 1 THIS IS THE STYLE CARDS I AM INTRESTED IN!!!
Please be creative, I am paying for my own eye catching design. I need files to be quilla press ready.

COLORS THAT ARE PAINTED INSIDE MY SHOP:
- - - http://www.brennacoat.example/en/explore-colors/painter/color-selector.html?colors=4007-3C

- - - http://www.marlowtint.example/color/paint-colors/quiet-harbor-d58-2

I want the business cards sleek and modern if you use the logo please correct imperfections. I added the part that says Blow Dry Bar (see website).
Do not be afraid to separate the blow dryer from the name to make the cards look like the file with the pink elephant.

SHOULD INCLUDE
*Blow Dryer (we are a blow dry bar not a salon we do not cut or color so do not include sheers of any kind)
*BUSINESS NAME: Simply Swept Up - Blow Dry Bar (PLEASE SEE MY WEBSITE)
* Website: SIMPLYSWEPTUP.EXAMPLE
*Phone number (555) 314-7720
Updates

Quilla press said it can be submitted in JPG

http://www.marlowtint.example/color/paint-colors/quiet-harbor-d58-2 http://www.brennacoat.example/en/explore-colors/painter/color-selector.html?colors=4007-3C ^^^^ These links will take you to the color paint that is painted inside my shop.

Target Market(s)

AGES 18 - 55 WOMEN
HIGH END MARKET

Industry/Entity Type

Salon

Requirements
Must have
• SEE COLOR EXAMPLE FILE
BLOW DRYER
UNIQUE
I LIKE THE CARD WITH THE PINK ELEPHANT THE BEST
Nice to have
• BE AS CREATIVE AND MODERN AS POSSIBLE DO NOT COPY ANY OF THE CARDS BELOW.
Should not have
• SCISSORS
PINK

```html
<!DOCTYPE html>
<html lang="en">
<head>
<meta charset="utf-8">
<title>Simply Swept Up – Business Cards</title>
<link rel="stylesheet" href="https://fonts.googleapis.com/css2?family=Arimo:wght@400;700&family=Rokkitt:wght@500&display=swap">
<style>
  :root {
    --page: #e9e6e1;
    --forest: #1f2d17;
    --forest-light: #2b3d20;
    --sun: #f2c40f;
    --sun-deep: #e8b40a;
    --photo-dark: #4a2a18;
    --photo-light: #b98560;
  }
  * { box-sizing: border-box; margin: 0; padding: 0; }
  html, body { width: 1200px; height: 960px; overflow: hidden; }
  body {
    background: var(--page);
    font-family: "Arimo", Arial, sans-serif;
    display: flex;
    flex-direction: column;
    align-items: center;
    justify-content: center;
    gap: 40px;
  }
  .card {
    position: relative;
    width: 700px;
    height: 400px;
    overflow: hidden;
    box-shadow: 0 6px 18px rgba(0,0,0,.18);
  }
  .brand-name {
    font-family: "Rokkitt", Georgia, serif;
    font-weight: 500;
    letter-spacing: .5px;
    display: flex;
    align-items: center;
    gap: 14px;
  }
  .brand-dot { width: 14px; height: 14px; border-radius: 50%; flex: none; }

  /* Offers card */
  .card--offers {
    background: linear-gradient(160deg, var(--forest-light), var(--forest) 60%);
    color: var(--sun);
    padding: 70px 60px;
  }
  .card--offers .brand-name { font-size: 58px; color: var(--sun); margin-bottom: 44px; }
  .card--offers .brand-dot { background: var(--sun); }
  .offer { margin-bottom: 18px; text-transform: uppercase; }
  .offer__title { font-size: 18px; line-height: 1.15; letter-spacing: .3px; }
  .offer__detail { font-size: 13px; line-height: 1.2; letter-spacing: .2px; }

  /* Contact card */
  .card--contact { background: var(--forest); }
  .card__shapes { position: absolute; inset: 0; }
  .card--contact .brand-name {
    position: absolute; right: 44px; top: 46px;
    font-size: 50px; color: var(--forest);
  }
  .card--contact .brand-dot { background: var(--forest); }
  .contact-list {
    position: absolute; right: 40px; top: 180px;
    list-style: none; text-align: right;
    color: var(--sun); font-size: 14px; line-height: 1.55;
    text-transform: uppercase; letter-spacing: .3px;
  }
  .contact-list li { display: flex; justify-content: flex-end; align-items: flex-start; gap: 10px; }
  .contact-list svg { width: 13px; height: 13px; margin-top: 3px; flex: none; fill: var(--sun); }
  .contact-list .address { line-height: 1.3; }
</style>
</head>
<body>

<section class="card card--offers">
  <div class="brand-name"><span>Simply Swept Up</span><span class="brand-dot"></span></div>
  <div class="offer">
    <p class="offer__title">Monday Madness</p>
    <p class="offer__detail">10% off all products purchased in store</p>
  </div>
  <div class="offer">
    <p class="offer__title">Thrifty Tuesday</p>
    <p class="offer__detail">$5.00 off your blow out service when you add any one upper</p>
  </div>
  <div class="offer">
    <p class="offer__title">Winedown Wednesday</p>
    <p class="offer__detail">Bring a friend, 2 blow outs for $60.00+tax</p>
  </div>
</section>

<section class="card card--contact">
  <svg class="card__shapes" viewBox="0 0 700 400" width="700" height="400">
    <defs>
      <linearGradient id="photo-tone" x1="0" y1="0" x2="1" y2="1">
        <stop offset="0" stop-color="var(--photo-dark)"/>
        <stop offset=".6" stop-color="var(--photo-light)"/>
        <stop offset="1" stop-color="#d8c9bd"/>
      </linearGradient>
    </defs>
    <polygon points="0,0 700,0 700,150 380,150 0,150" fill="var(--sun)"/>
    <polygon points="0,150 380,150 470,400 0,400" fill="url(#photo-tone)" role="img" aria-label="Photo of a woman having her long hair blow dried"/>
  </svg>

  <div class="brand-name"><span>Simply Swept Up</span><span class="brand-dot"></span></div>

  <ul class="contact-list">
    <li><span>(555) 314-7720</span>
      <svg viewBox="0 0 24 24"><path d="M6.6 10.8a15 15 0 0 0 6.6 6.6l2.2-2.2a1 1 0 0 1 1-.3 11.4 11.4 0 0 0 3.6.6 1 1 0 0 1 1 1V20a1 1 0 0 1-1 1A17 17 0 0 1 3 4a1 1 0 0 1 1-1h3.5a1 1 0 0 1 1 1c0 1.3.2 2.5.6 3.6a1 1 0 0 1-.3 1z"/></svg></li>
    <li><span>Simplysweptup.example</span>
      <svg viewBox="0 0 24 24"><path d="M12 2a10 10 0 1 0 0 20 10 10 0 0 0 0-20zm6.9 6h-3a15 15 0 0 0-1.3-3.9A8 8 0 0 1 18.9 8zM12 4c.8 1.2 1.5 2.5 1.9 4h-3.8c.4-1.5 1.1-2.8 1.9-4zM4.3 14a8 8 0 0 1 0-4h3.4a16 16 0 0 0 0 4zm.8 2h3a15 15 0 0 0 1.3 3.9A8 8 0 0 1 5.1 16zm3-8h-3a8 8 0 0 1 4.3-3.9A15 15 0 0 0 8.1 8zM12 20c-.8-1.2-1.5-2.5-1.9-4h3.8c-.4 1.5-1.1 2.8-1.9 4zm2.3-6H9.7a14 14 0 0 1 0-4h4.6a14 14 0 0 1 0 4zm.3 5.9a15 15 0 0 0 1.3-3.9h3a8 8 0 0 1-4.3 3.9zM16.3 14a16 16 0 0 0 0-4h3.4a8 8 0 0 1 0 4z"/></svg></li>
    <li><span>Info@simplysweptup.example</span>
      <svg viewBox="0 0 24 24"><path d="M2 5h20v14H2zm2 2v.4l8 5 8-5V7zm0 2.8V17h16V9.8l-8 5z"/></svg></li>
    <li><span class="address">82 Heron Bay Drive Suite 4<br>Maple Hollow, Texas 70001</span>
      <svg viewBox="0 0 24 24"><path d="M12 2a7 7 0 0 0-7 7c0 5.2 7 13 7 13s7-7.8 7-13a7 7 0 0 0-7-7zm0 9.5A2.5 2.5 0 1 1 12 6.5a2.5 2.5 0 0 1 0 5z"/></svg></li>
  </ul>
</section>

</body>
</html>
```